Design and built Guitarlesson compare website

Hi,

I would like to have an "affiliate guitarlesson websites".
I have (tried) to make a concept myself, the idea is oke but still not effective ([login to view URL]) not live

Some items I would like to see:
- website built with Bootstrap.
- good SEO /Conversion Optimisation
- visitors must be able to add comments to the lesson*
- visitors must be able to rate the lessen*
- website should be with guitar images (including rights)
- I think one page would be oke but if you have beter solutions just name it, maby one for the total and one with the lesson information (rate and comments)

* I will write the php script and connection to the database myself

If you have any questions don't hesitate to contact me.

Rik

```html
<!DOCTYPE html>
<html lang="en">
<head>
<meta charset="utf-8">
<title>Guitar Lesson</title>
<link rel="stylesheet" href="https://fonts.googleapis.com/css2?family=Roboto:wght@300;400;500&family=Arimo:wght@400;700&display=swap">
<style>
:root{
  --white:#ffffff;
  --ink:#1a1a1a;
  --text:#444444;
  --muted:#777777;
  --nav-text:#555555;
  --nav-active:#f2f2f2;
  --black:#000000;
  --cat-text:#bbbbbb;
  --accent:#e0501e;
  --band:#2e2e2e;
  --silhouette:#f7964f;
  --footer:#333333;
  --footer-bottom:#222222;
  --footer-text:#d0d0d0;
  --footer-line:#555555;
}
*{box-sizing:border-box;margin:0;padding:0}
html,body{width:1200px;height:2396px;overflow:hidden;background:var(--white)}
body{position:relative;font-family:'Roboto',sans-serif;color:var(--ink)}

/* nav */
.site-nav{position:absolute;left:0;top:0;width:1200px;height:67px;background:var(--white)}
.brand{position:absolute;left:112px;top:18px;font-size:22px;font-weight:400;color:var(--ink)}
.nav-item{position:absolute;top:0;height:62px;line-height:62px;font-size:12px;letter-spacing:.6px;color:var(--nav-text);transform:translateX(-50%);white-space:nowrap}
.nav-item.active{background:var(--nav-active);padding:0 12px}

/* hero */
.hero-photo{position:absolute;left:0;top:67px;width:1200px;height:589px;
  background:radial-gradient(ellipse at 65% 40%,#5a3020 0%,#2a1208 35%,#0a0302 70%,#000 100%)}
.category-bar{position:absolute;left:0;top:656px;width:1200px;height:107px;background:var(--black)}
.category{position:absolute;top:20px;width:110px;margin-left:-55px;text-align:center;color:var(--cat-text);font-family:'Arimo',sans-serif;font-weight:700;font-size:12.5px}
.category svg{display:block;margin:0 auto 10px;width:24px;height:24px;fill:var(--cat-text)}

/* welcome */
.welcome-title{position:absolute;left:0;width:1200px;top:845px;text-align:center;font-family:'Arimo',sans-serif;font-weight:400;font-size:40px;letter-spacing:1.5px;color:var(--ink);line-height:48px}
.welcome-title span{border-bottom:2px solid var(--ink);padding-bottom:1px}
.lesson{position:absolute;top:960px;width:260px;margin-left:-130px;text-align:center}
.lesson-icon{display:block;margin:0 auto;width:60px;height:60px}
.lesson-name{margin-top:22px;font-size:22px;letter-spacing:.5px;color:var(--ink)}
.rating{display:flex;justify-content:center;gap:5px;margin-top:18px}
.rating svg{width:37px;height:37px}
.comment-btn{display:block;margin:12px auto 0;width:237px;height:44px;border:1px solid #bbb;border-radius:6px;background:var(--white);font-family:'Roboto',sans-serif;font-size:22px;color:var(--ink);letter-spacing:.5px}
.col-divider{position:absolute;top:973px;width:1px;height:127px;background:#e2e2e2}

/* testimonials */
.accent-line{position:absolute;left:0;top:1253px;width:1200px;height:7px;background:var(--accent)}
.testimonial-band{position:absolute;left:0;top:1260px;width:1200px;height:209px;background:var(--band);overflow:hidden}
.testimonial-card{position:absolute;left:93px;top:1260px;width:407px;height:153px;background:var(--accent);border-radius:0 0 4px 4px;padding:24px 14px 0 14px;color:var(--white)}
.testimonial-card h2{font-family:'Roboto',sans-serif;font-weight:300;font-size:26px;margin-bottom:8px}
.testimonial-card p{font-family:'Arimo',sans-serif;font-size:12px;line-height:18px}
.tablet{position:absolute;left:607px;top:27px;width:267px;height:182px;background:#0b0b0b;border-radius:14px 14px 0 0;border:2px solid #444;border-bottom:none}
.tablet-screen{position:absolute;left:20px;top:18px;right:20px;bottom:0;background:linear-gradient(180deg,#f4f4f4 0 10%,#3a4a6a 10%,#6a5a7a 55%,#c87a3a 100%)}

/* about */
.about-title{position:absolute;left:0;width:1200px;top:1518px;text-align:center;font-weight:300;font-size:50px;color:var(--text)}
.about-figure{position:absolute;left:91px;top:1624px;width:410px;height:317px;background:radial-gradient(ellipse at 50% 50%,var(--silhouette) 0 55%,#fbc39a 100%)}
.about-q{position:absolute;left:698px;font-weight:300;font-size:20px;color:var(--muted)}
.about-a{position:absolute;left:698px;font-family:'Arimo',sans-serif;font-size:18px;letter-spacing:.8px;color:var(--ink)}

/* footer */
.site-footer{position:absolute;left:0;top:2005px;width:1200px;height:351px;background:var(--footer);font-family:'Arimo',sans-serif;color:var(--footer-text)}
.footer-bottom{position:absolute;left:0;top:2356px;width:1200px;height:40px;background:var(--footer-bottom);font-family:'Arimo',sans-serif;font-size:12px;color:var(--white);padding:14px 0 0 93px}
.f-title{position:absolute;font-family:'Roboto',sans-serif;font-size:16px;color:var(--white)}
.f-lead{position:absolute;left:93px;top:67px;width:330px;font-size:12px;line-height:17px;font-weight:700;color:var(--white)}
.f-para{position:absolute;left:93px;width:330px;font-size:11px;line-height:16px}
.f-rule{position:absolute;left:93px;top:291px;width:320px;height:1px;background:var(--footer-line)}
.quick-links{position:absolute;left:532px;top:70px;list-style:disc outside;font-size:11.5px;line-height:16px;color:var(--footer-text)}
.f-divider{position:absolute;left:760px;top:44px;width:1px;height:307px;background:var(--footer-line)}
.map{position:absolute;top:70px;width:133px;height:88px;background:linear-gradient(135deg,#e8e4d8,#d4dcc8 60%,#c8d4e0)}
.email-label{position:absolute;left:787px;top:199px;font-size:13px;font-weight:700;color:var(--white)}
.social{position:absolute;top:197px;width:18px;height:18px;border:2px solid var(--white);border-radius:3px}
.field{position:absolute;height:23px;border:1px solid #4a4a4a;background:#2c2c2c;font-size:11px;color:#999;padding:4px 8px}
.send-btn{position:absolute;left:1001px;top:308px;width:106px;height:30px;background:#999;border-radius:4px;color:var(--white);font-size:12px;text-align:center;line-height:30px}
</style>
</head>
<body>

<header class="site-nav">
  <div class="brand">logo</div>
  <span class="nav-item active" style="left:653px">Home</span>
  <span class="nav-item" style="left:721px">Features</span>
  <span class="nav-item" style="left:800px">About Us</span>
  <span class="nav-item" style="left:879px">Out team</span>
  <span class="nav-item" style="left:976px">Plans &amp; Pricing</span>
  <span class="nav-item" style="left:1071px">Support</span>
</header>

<div class="hero-photo" role="img" aria-label="Close-up photo of hands playing an electric guitar fretboard"></div>

<nav class="category-bar">
  <div class="category" style="left:159px"><svg viewBox="0 0 24 24"><path d="M2 4h3l2 10h12l2-8H7" fill="none" stroke="#bbb" stroke-width="2.5"/><circle cx="9" cy="19" r="2"/><circle cx="17" cy="19" r="2"/></svg>Commerce</div>
  <div class="category" style="left:269px"><svg viewBox="0 0 24 24"><rect x="2" y="7" width="20" height="14" rx="2"/><rect x="8" y="3" width="8" height="5" fill="none" stroke="#bbb" stroke-width="2"/></svg>Business</div>
  <div class="category" style="left:379px"><svg viewBox="0 0 24 24"><path d="M3 9h5l10-5v16L8 15H3z"/><rect x="6" y="15" width="3" height="6"/></svg>Marketing</div>
  <div class="category" style="left:489px"><svg viewBox="0 0 24 24"><text x="12" y="21" text-anchor="middle" font-size="22" font-family="Arimo,sans-serif" font-weight="700" fill="#bbb">$</text></svg>Finance</div>
  <div class="category" style="left:599px"><svg viewBox="0 0 24 24"><path d="M8 4l12-2v14h-2V6L10 7v11H8z"/><circle cx="6" cy="18" r="3"/><circle cx="17" cy="16" r="3"/></svg>Music</div>
  <div class="category" style="left:709px"><svg viewBox="0 0 24 24"><path d="M12 4L1 9l11 5 11-5z"/><path d="M5 12v5c3 3 11 3 14 0v-5l-7 3z"/></svg>Publishing</div>
  <div class="category" style="left:819px"><svg viewBox="0 0 24 24"><path d="M12 3L1 12h3v9h6v-6h4v6h6v-9h3z"/></svg>Real Estate</div>
  <div class="category" style="left:929px"><svg viewBox="0 0 24 24"><path d="M4 2h2v7h1V2h2v7h1V2h2v9l-2 2v9H8v-9l-4-2z"/><path d="M16 2c3 0 4 4 4 8h-2v12h-2z"/></svg>Restaurant</div>
  <div class="category" style="left:1039px"><svg viewBox="0 0 24 24"><path d="M21 3l-5 5-11-3-2 2 9 5-4 4-3-1-2 2 4 2 2 4 2-2-1-3 4-4 5 9 2-2-3-11 5-5z"/></svg>Travel</div>
</nav>

<main>
  <h1 class="welcome-title"><span>WELCOME TO GUITAR LESSON</span></h1>

  <div class="col-divider" style="left:440px"></div>
  <div class="col-divider" style="left:773px"></div>

  <section class="lesson" style="left:251px">
    <svg class="lesson-icon" viewBox="0 0 60 60"><g fill="#888"><path d="M40 4h16v16l-6-6-10 10-4-4 10-10z"/><path d="M20 56H4V40l6 6 10-10 4 4-10 10z"/></g></svg>
    <div class="lesson-name">Lesson 1</div>
    <div class="rating">
      <svg viewBox="0 0 24 24"><use href="#star"/></svg><svg viewBox="0 0 24 24"><use href="#star"/></svg><svg viewBox="0 0 24 24"><use href="#star"/></svg><svg viewBox="0 0 24 24"><use href="#star"/></svg><svg viewBox="0 0 24 24"><use href="#star"/></svg>
    </div>
    <button class="comment-btn">Add Comment</button>
  </section>

  <section class="lesson" style="left:601px">
    <svg class="lesson-icon" viewBox="0 0 60 60"><path d="M56 4L6 28l18 6 6 20z" fill="#aaa"/><path d="M56 4L24 34l6 20z" fill="#888"/></svg>
    <div class="lesson-name">Lesson 2</div>
    <div class="rating">
      <svg viewBox="0 0 24 24"><use href="#star"/></svg><svg viewBox="0 0 24 24"><use href="#star"/></svg><svg viewBox="0 0 24 24"><use href="#star"/></svg><svg viewBox="0 0 24 24"><use href="#star"/></svg><svg viewBox="0 0 24 24"><use href="#star"/></svg>
    </div>
    <button class="comment-btn">Add Comment</button>
  </section>

  <section class="lesson" style="left:939px">
    <svg class="lesson-icon" viewBox="0 0 60 60"><path d="M30 52L8 30C0 22 6 8 17 8c6 0 10 4 13 8 3-4 7-8 13-8 11 0 17 14 9 22z" fill="none" stroke="#888" stroke-width="6" stroke-linejoin="round"/></svg>
    <div class="lesson-name">Lesson 3</div>
    <div class="rating">
      <svg viewBox="0 0 24 24"><use href="#star"/></svg><svg viewBox="0 0 24 24"><use href="#star"/></svg><svg viewBox="0 0 24 24"><use href="#star"/></svg><svg viewBox="0 0 24 24"><use href="#star"/></svg><svg viewBox="0 0 24 24"><use href="#star"/></svg>
    </div>
    <button class="comment-btn">Add Comment</button>
  </section>

  <svg width="0" height="0" style="position:absolute">
    <defs>
      <linearGradient id="starFill" x1="0" y1="0" x2="0" y2="1">
        <stop offset="0" stop-color="#ffe14d"/><stop offset="1" stop-color="#f2a800"/>
      </linearGradient>
      <path id="star" d="M12 1.5l3.1 6.9 7.4.7-5.6 5 1.7 7.4L12 17.6l-6.6 3.9 1.7-7.4-5.6-5 7.4-.7z" fill="url(#starFill)" stroke="#c98a00" stroke-width=".6"/>
    </defs>
  </svg>

  <div class="accent-line"></div>
  <section class="testimonial-band">
    <div class="tablet"><div class="tablet-screen" role="img" aria-label="Tablet showing a responsive website preview"></div></div>
  </section>
  <div class="testimonial-card">
    <h2>What people are saying...</h2>
    <p>Mobile projects deserve to be shared, to be criticized, and to be refined. Save and access them anywhere from the cloud and share with team members, developers, and designers alike. Present your live previews to stakeholders for testing and feedback.</p>
  </div>

  <h2 class="about-title">About Us</h2>
  <div class="about-figure" role="img" aria-label="Orange silhouette of a guitarist raising a guitar in triumph"></div>
  <div class="about-q" style="top:1671px">Who are we?</div>
  <div class="about-a" style="top:1721px">TEXT WILL COME</div>
  <div class="about-q" style="top:1846px">How we work...</div>
  <div class="about-a" style="top:1900px">TEXT WILL COME</div>
</main>

<footer class="site-footer">
  <div class="f-title" style="left:93px;top:43px">About us</div>
  <div class="f-lead">We're a company providing business software solutions to individuals and large companies</div>
  <p class="f-para" style="top:127px">It has survived not only five centuries, but also the leap into electronic typesetting, remaining essentially remaining essentially unchanged unchanged.remaining essentially unchanged.</p>
  <p class="f-para" style="top:200px">We have offices around the world.Our experience leads us to believe that a thoughtful combination of both algorithmic and human skills offers the best means in a space as broad as business technology.</p>
  <div class="f-rule"></div>

  <div class="f-title" style="left:497px;top:45px">Quick links</div>
  <ul class="quick-links">
    <li>Home</li><li>Features</li><li>About Us</li><li>Out team</li><li>Plans &amp; Pricing</li><li>Support</li>
  </ul>

  <div class="f-divider"></div>

  <div class="f-title" style="left:787px;top:43px">How to contact us?</div>
  <div class="map" style="left:787px" role="img" aria-label="Street map of the first office location"></div>
  <div class="map" style="left:960px" role="img" aria-label="Street map of the second office location"></div>

  <div class="email-label">Email us</div>
  <div class="social" style="left:954px"></div>
  <div class="social" style="left:996px"></div>
  <div class="social" style="left:1039px"></div>
  <div class="social" style="left:1082px"></div>

  <div class="field" style="left:787px;top:228px;width:146px">Name</div>
  <div class="field" style="left:960px;top:228px;width:147px">Email</div>
  <div class="field" style="left:787px;top:259px;width:320px;height:40px"></div>
  <div class="send-btn">Send message</div>
</footer>
<div class="footer-bottom">News | Tune Shop | Marketplace</div>

</body>
</html>
```